Business Card Design

Im electrician in melbourne after a business cards. I have no logos done. I have attached a card that i like but needs to be altered to my business name, so in the picture shows a lead plug into a socket spelling plug, i want the spelling replaced with my company name. I was thinking some thing with a charcoal back ground with yellow or green font.
I have wrote what I'd like above but feel free to try your own ideas and designs.
Industry/Entity Type
Electrician
Contact Information for Business Card
Zul Electrical Services PTY LTD (Display on the front of card, the PTY LTD can be in small font)
REC:58142 (also on the front in small font)
Call Dario (back i dont want my last name on the card)
Phone: 0488157093 (back
Email: zulelectricalservices@kestrelmail.net (back)
Domestic, Commercial, Industrial, (on the back in dot points.)
Look and feel
Each slider illustrates characteristics of the customer's brand and the style your logo design should communicate.

```html
<!DOCTYPE html>
<html lang="en">
<head>
<meta charset="utf-8">
<title>Zul Electrical Services – Business Card Back</title>
<link rel="stylesheet" href="https://fonts.googleapis.com/css2?family=Didact+Gothic&family=Arimo:wght@400&display=swap">
<style>
  :root {
    --card-centre: #b2b2b2;
    --card-mid: #949494;
    --card-edge: #727170;
    --band: #4b4949;
    --ink: #ffffff;
  }
  html, body {
    margin: 0;
    padding: 0;
    width: 1200px;
    height: 727px;
    overflow: hidden;
    background: var(--card-edge);
  }
  .card {
    display: block;
    width: 1200px;
    height: 727px;
  }
  .contact-name {
    font-family: "Didact Gothic", "Century Gothic", sans-serif;
    font-weight: 700;
    font-size: 62px;
    fill: var(--ink);
  }
  .contact-line {
    font-family: "Didact Gothic", "Century Gothic", sans-serif;
    font-weight: 400;
    fill: var(--ink);
  }
  .contact-phone { font-size: 52px; }
  .contact-email { font-size: 45px; }
  .contact-icon {
    fill: none;
    stroke: var(--ink);
    stroke-width: 2.2;
    stroke-linejoin: round;
    stroke-linecap: round;
  }
  .service-band { fill: var(--band); }
  .service-label {
    font-family: "Arimo", Arial, sans-serif;
    font-size: 42px;
    fill: var(--ink);
  }
</style>
</head>
<body>
<svg class="card" viewBox="0 0 1200 727" xmlns="http://www.w3.org/2000/svg">
  <defs>
    <radialGradient id="card-glow" cx="600" cy="330" r="720" gradientUnits="userSpaceOnUse">
      <stop offset="0" stop-color="var(--card-centre)"/>
      <stop offset="0.45" stop-color="var(--card-mid)"/>
      <stop offset="1" stop-color="var(--card-edge)"/>
    </radialGradient>
  </defs>

  <rect class="card-background" width="1200" height="727" fill="url(#card-glow)"/>

  <text class="contact-name" x="617" y="261" text-anchor="middle">Call Dario</text>

  <g class="contact-icon phone-icon" transform="translate(100 306)">
    <path d="M4 20 C4 6 54 6 54 20 L54 26 L42 26 L42 19 L16 19 L16 26 L4 26 Z"/>
    <path d="M14 24 L8 46 L50 46 L44 24 Z"/>
    <circle cx="29" cy="34" r="7"/>
    <circle cx="29" cy="34" r="2.5"/>
  </g>
  <text class="contact-line contact-phone" x="617" y="358" text-anchor="middle">0488157093</text>

  <g class="contact-icon mail-icon" transform="translate(102 424)">
    <rect x="0" y="0" width="54" height="30" rx="2"/>
    <path d="M0 1 L27 18 L54 1"/>
    <path d="M0 29 L20 13 M54 29 L34 13"/>
  </g>
  <text class="contact-line contact-email" x="678" y="454" text-anchor="middle">zulelectricalservices@kestrelmail.net</text>

  <rect class="service-band" x="0" y="662" width="1200" height="65"/>
  <text class="service-label" x="37" y="709">DOMESTIC</text>
  <text class="service-label" x="590" y="709" text-anchor="middle">COMMERCIAL</text>
  <text class="service-label" x="1164" y="709" text-anchor="end">INDUSTRIAL</text>
</svg>
</body>
</html>
```